Business Card Design

we are a wellness center offering therapeutic massage modalities and yoga and meditation classes. I would like to see designs that incorporate the colors of my current logo (image uploaded) BUT I would like to change my logo slightly so that the three words wrapping around my image are: massage yoga wellness (in other words, take out skin).

Industry/Entity Type

Massage

Contact Information for Business Card

Lena R. Calloway, BS, CMT, E-RYT, Owner
427 E. Brindle Ave., Suite 3C
Hampton, VA 23581
757-302-5594 (office)
757-861-2047 (cell)
fernleafrestorative.example
fernleafrestorative@mailbox.example

Requirements
Nice to have
• I'd like to have my logo as a watermark on the back side, but if that's not doable, no big deal. Thanks.

```html
<!DOCTYPE html>
<html lang="en">
<head>
<meta charset="utf-8">
<title>Fernleaf Restorative — Business Card</title>
<link rel="stylesheet" href="https://fonts.googleapis.com/css2?family=Arimo:wght@400;700&display=swap">
<style>
  :root {
    --backdrop: #c5d2dc;
    --card-white: #f7f7f8;
    --peach: #e8c89b;
    --band-peach: #ecca98;
    --teal: #7ea3b1;
    --rust: #c9603f;
    --figure-grey: #bab8a6;
    --shadow: rgba(60, 80, 100, 0.22);
  }
  * { box-sizing: border-box; margin: 0; padding: 0; }
  html, body {
    width: 1200px; height: 840px; overflow: hidden;
    background: var(--backdrop);
    font-family: "Arimo", Arial, sans-serif;
  }
  .stage {
    position: relative; width: 1200px; height: 840px;
    display: flex; align-items: center; justify-content: center; gap: 40px;
  }
  .card {
    position: relative; width: 540px; height: 309px; overflow: hidden;
    box-shadow: 0 10px 28px var(--shadow);
  }
  /* back side */
  .card--back { background: var(--card-white); }
  .card--back .brand { position: absolute; left: 150px; top: 38px; }
  .card--back .accent-band {
    position: absolute; left: 0; right: 0; top: 112px; height: 34px;
    background: var(--band-peach);
  }
  .contact {
    position: absolute; left: 34px; top: 170px;
    list-style: none; color: var(--rust);
    font-size: 13px; font-weight: 700; line-height: 1.5;
  }
  .contact .owner { font-size: 14px; }
  /* front side */
  .card--front { background: var(--peach); }
  .card--front .brand { position: absolute; left: 40px; top: 124px; }
  .figure-area {
    position: absolute; right: 0; top: 0; width: 220px; height: 309px;
    background: radial-gradient(ellipse at 55% 65%, var(--figure-grey) 0%, var(--figure-grey) 45%, var(--peach) 80%);
  }
  /* brand lockup */
  .brand { display: flex; align-items: center; gap: 12px; }
  .brand-mark {
    width: 52px; height: 52px; border-radius: 50%; background: var(--teal);
    flex: none;
  }
  .brand-name {
    color: var(--teal); font-size: 26px; font-weight: 400; line-height: 1.05;
  }
  .card--back .brand-mark { width: 40px; height: 40px; }
  .card--back .brand-name { font-size: 21px; }
</style>
</head>
<body>
<main class="stage">
  <section class="card card--back" aria-label="Business card, back">
    <div class="brand">
      <span class="brand-mark" aria-hidden="true"></span>
      <span class="brand-name">Fernleaf<br>Restorative</span>
    </div>
    <div class="accent-band" aria-hidden="true"></div>
    <ul class="contact">
      <li class="owner">Lena R. Calloway, BS, CMT, E-RYT, Owner</li>
      <li>Office: 757-302-5594</li>
      <li>Cell: 757-861-2047</li>
      <li>Email: fernleafrestorative@mailbox.example</li>
      <li>Url: fernleafrestorative.example</li>
    </ul>
  </section>

  <section class="card card--front" aria-label="Business card, front">
    <div class="figure-area" role="img" aria-label="Grey silhouette of a person seated in a cross-legged meditation pose"></div>
    <div class="brand">
      <span class="brand-mark" aria-hidden="true"></span>
      <span class="brand-name">Fernleaf<br>Restorative</span>
    </div>
  </section>
</main>
</body>
</html>
```